Buchungsplattform für Hypnose-Dienstleistungen sucht Zertifikat-Design
Zielgruppe
Buchungsplattform für Hypnose Dienstleistungen. Die Zielgruppe des angeklagten Design (Zertifikat) geht an registrierte Anbieter (Hypnosetherapeuten, Praxes, Zahnärzte, etc).
Aufgabenstellung
Das gewünschte Zertifikat soll;
- unser CI/CD berücksichtigen (Primär Orange: #DD3200 Sekundär Blau: #0085A8(
- soll einen wertvollen, aufwendigen, besonderen Eindruck vermitteln
- soll sich inhaltlich in etwa dem angehängten Vorschlag orientieren
- kann spezielle Druckverfahren (Prägedruck, Stanz, Laser, etc. ) in Erwägung ziehen wo angebracht

```html
<!DOCTYPE html>
<html lang="de">
<head>
<meta charset="utf-8">
<title>Certificate of Excellence – Somnaris</title>
<link href="https://fonts.googleapis.com/css2?family=EB+Garamond:wght@400;500;700&display=swap" rel="stylesheet">
<style>
  :root {
    --orange: #e04a1c;
    --blue: #0a679c;
    --ink: #111111;
    --paper: #ffffff;
    --gold-light: #f2e07a;
    --gold: #d9bf3c;
    --gold-dark: #a88a1c;
    --wave: #f3c2b0;
  }
  * { margin: 0; padding: 0; box-sizing: border-box; }
  html, body { width: 848px; height: 1200px; overflow: hidden; background: var(--paper); }
  .certificate {
    position: relative;
    width: 848px;
    height: 1200px;
    background: var(--paper);
    border: 1px solid #cfcfcf;
    font-family: "EB Garamond", Georgia, serif;
    color: var(--ink);
    overflow: hidden;
  }
  .brand {
    position: absolute;
    top: 62px;
    left: 0;
    width: 100%;
    display: flex;
    justify-content: center;
    align-items: center;
    gap: 14px;
  }
  .brand-name {
    font-size: 72px;
    font-weight: 500;
    letter-spacing: 6px;
    color: var(--orange);
    line-height: 1;
  }
  .brand-dot {
    width: 16px;
    height: 16px;
    border-radius: 50%;
    background: var(--orange);
  }
  .title {
    position: absolute;
    top: 252px;
    left: 0;
    width: 100%;
    text-align: center;
    font-size: 74px;
    font-weight: 700;
    line-height: 78px;
    color: var(--blue);
    letter-spacing: 1px;
  }
  .practice-name {
    position: absolute;
    top: 494px;
    left: 0;
    width: 100%;
    text-align: center;
    font-size: 60px;
    font-weight: 400;
    line-height: 70px;
  }
  .practice-rule {
    position: absolute;
    top: 574px;
    left: 175px;
    width: 498px;
    height: 2px;
    background: linear-gradient(90deg, transparent, var(--orange) 15%, var(--orange) 85%, transparent);
  }
  .holder {
    position: absolute;
    top: 594px;
    left: 0;
    width: 100%;
    text-align: center;
    font-size: 21px;
    line-height: 29px;
    letter-spacing: 0.3px;
  }
  .citation {
    position: absolute;
    top: 696px;
    left: 0;
    width: 100%;
    text-align: center;
    font-size: 36px;
    line-height: 46px;
  }
  .waves {
    position: absolute;
    left: 0;
    top: 860px;
    width: 848px;
    height: 340px;
  }
  .issuer-rule {
    position: absolute;
    top: 960px;
    left: 68px;
    width: 266px;
    height: 2px;
    background: linear-gradient(90deg, transparent, var(--orange) 15%, var(--orange) 85%, transparent);
  }
  .issuer {
    position: absolute;
    top: 972px;
    left: 99px;
    font-size: 19px;
    line-height: 24px;
    letter-spacing: 0.2px;
  }
  .seal {
    position: absolute;
    left: 0;
    top: 0;
    width: 848px;
    height: 1200px;
    pointer-events: none;
  }
</style>
</head>
<body>
<main class="certificate">
  <header class="brand">
    <span class="brand-name">SOMNARIS</span>
    <span class="brand-dot"></span>
  </header>

  <h1 class="title">CERTIFICATE<br>OF EXELLENCE</h1>

  <p class="practice-name">Praxisname</p>
  <div class="practice-rule"></div>
  <p class="holder">VORNAME&nbsp; NACHNAME<br>ADRESSE &nbsp;&nbsp;/&nbsp;&nbsp;&nbsp; PLZ ORT</p>

  <p class="citation">wird für seine hervorragende Qualität<br>und Betriebsleistung anerkannt.</p>

  <svg class="waves" viewBox="0 0 848 340" role="img" aria-label="Feine geschwungene Linienornamente in zartem Orange">
    <defs>
      <linearGradient id="waveTone" x1="0" y1="0" x2="1" y2="1">
        <stop offset="0" stop-color="#fdf1ec" stop-opacity="0"/>
        <stop offset="0.5" stop-color="#fbe3d9" stop-opacity="0.7"/>
        <stop offset="1" stop-color="#fdf1ec" stop-opacity="0.2"/>
      </linearGradient>
    </defs>
    <path d="M0 180 C 220 250 420 60 848 30 L 848 340 L 0 340 Z" fill="url(#waveTone)"/>
  </svg>

  <div class="issuer-rule"></div>
  <p class="issuer">SOMNARIS SCHWEIZ AG<br>QUALITY ASSURANCE</p>

  <svg class="seal" viewBox="0 0 848 1200" aria-hidden="true">
    <defs>
      <linearGradient id="ribbonGold" x1="0" y1="0" x2="1" y2="1">
        <stop offset="0" stop-color="var(--gold-dark)"/>
        <stop offset="0.35" stop-color="var(--gold-light)"/>
        <stop offset="0.7" stop-color="var(--gold)"/>
        <stop offset="1" stop-color="var(--gold-dark)"/>
      </linearGradient>
      <radialGradient id="sealGold" cx="0.45" cy="0.4" r="0.65">
        <stop offset="0" stop-color="#f7ea95"/>
        <stop offset="0.6" stop-color="var(--gold)"/>
        <stop offset="1" stop-color="var(--gold-dark)"/>
      </radialGradient>
    </defs>
    <polygon points="848,800 848,860 498,1200 458,1200" fill="url(#ribbonGold)"/>
    <circle cx="670" cy="1022" r="112" fill="url(#sealGold)"/>
  </svg>
</main>
</body>
</html>
```